Granite Tile Retail Website

We need wireframe PSD for a website selling granite tile. There are 4 custom pages, shopping cart page, and checkout page. I have a logo designed but the color scheme is up to you.
Please look at design-explanation.docx as I got through each page with more detail.
Home - I mocked up the home page so you know the layout (lg-home.jpg). This is where I need you to spend the most time to make a very appealing design.
Color Gallery - We have approximately 20 different stone colors. Each color will have a little gallery of its own pictures. On this page the customer can also add a sample piece of the color they are viewing to their shopping cart.
Questions Page - This page has 3 elements
1. Upload or fax diagram of kitchen for quotation
2. Installation video
3. Installation FAQ (text)
Order Page - This page has 3 steps for the customer
1. Customer chooses his color.
2. For each color we have numerous different products. He inputs the quantity of each product.
3. Customer is given total price and shipping quote. If order over $500 it says "This order qualifies for free shipping". Customer can click on button to "Order Now"
Shopping Cart - Very standard, just like I have attached here. Just modify for your colors / font.
Checkout - Just like in the attached. See design-explanation.docx for minor adjustments.
I have vector file for logo.
Updates
Please try to post your designs by tonightÂ
Target Market(s)
Home owners 40-60 years old
Industry/Entity Type
Shopping
Look and feel

```html
<!DOCTYPE html>
<html lang="en">
<head>
<meta charset="utf-8">
<title>Granite Tile – Home</title>
<link rel="stylesheet" href="https://fonts.googleapis.com/css2?family=Arimo:wght@400;700&display=swap">
<style>
  :root {
    --canvas: #ffffff;
    --page: #ececec;
    --footer: #e1e1e1;
    --footer-line: #c9c9c9;
    --logo: #b3b3b3;
    --nav: #a9a9a9;
    --nav-active: #bdbdbd;
    --nav-text: #d2d2d2;
    --video: #646464;
    --card: #3d3d3d;
    --text: #8a8a8a;
    --text-soft: #9a9a9a;
    --text-dark: #666666;
    --btn-top: #d6d6d6;
    --btn-bottom: #9c9c9c;
    --btn-text: #333333;
    --white: #ffffff;
    --black: #2a2a2a;
  }
  * { box-sizing: border-box; margin: 0; padding: 0; }
  html, body { width: 873px; height: 1200px; overflow: hidden; background: var(--canvas); }
  body { font-family: "Arimo", Arial, sans-serif; position: relative; }
  .page { position: absolute; left: 14px; top: 25px; width: 848px; height: 1155px; background: var(--page); }
  .abs { position: absolute; }

  .logo { background: var(--logo); border-radius: 12px; color: var(--white); display: flex; align-items: center; justify-content: center; font-size: 42px; letter-spacing: 1px; }
  .logo--header { left: 38px; top: 52px; width: 200px; height: 98px; }
  .logo--footer { left: 642px; top: 988px; width: 201px; height: 98px; }

  .account { top: 43px; left: 626px; font-size: 16px; color: var(--text-soft); }
  .account span + span { margin-left: 16px; }

  .search-label { left: 600px; top: 101px; font-size: 16px; color: var(--text-soft); }
  .search-field { left: 660px; top: 95px; width: 136px; height: 31px; background: var(--white); border: 1px solid #aaaaaa; }
  .search-go { left: 799px; top: 94px; width: 33px; height: 33px; border-radius: 50%; background: var(--black); color: var(--white); font-weight: 700; font-size: 14px; display: flex; align-items: center; justify-content: center; box-shadow: inset 0 0 0 2px #555; }

  .nav a { position: absolute; top: 172px; height: 36px; border-radius: 14px; background: var(--nav); color: var(--nav-text); font-size: 15px; display: flex; align-items: center; justify-content: center; text-decoration: none; }
  .nav a.is-active { background: var(--nav-active); color: var(--white); }

  .video { left: 42px; top: 241px; width: 558px; height: 322px; border-radius: 12px; background: var(--video); }
  .video svg { position: absolute; left: 296px; top: 373px; }

  .intro { left: 615px; width: 226px; font-size: 14.5px; line-height: 17.3px; color: var(--text); }

  .card { top: 591px; height: 238px; background: var(--card); border-radius: 6px; }
  .card-photo { position: absolute; top: 19px; height: 150px; }
  .card-button { position: absolute; top: 182px; height: 43px; border-radius: 6px; background: linear-gradient(var(--btn-top), var(--btn-bottom)); color: var(--btn-text); font-weight: 700; font-size: 19px; display: flex; align-items: center; justify-content: center; gap: 10px; }
  .card-button svg { flex: none; }

  .about { left: 49px; top: 857px; width: 790px; font-size: 15.5px; line-height: 18.4px; color: var(--text); }

  .footer { left: 14px; top: 980px; width: 848px; height: 200px; background: var(--footer); border-top: 1px solid var(--footer-line); }
  .footer-links { top: 988px; font-size: 16.5px; line-height: 22.3px; color: var(--text-soft); text-align: center; list-style: none; }
  .copyright { left: 474px; top: 1156px; font-size: 16px; color: var(--text-dark); }
  .copyright span { margin-left: 8px; }
</style>
</head>
<body>
  <div class="page"></div>

  <div class="abs logo logo--header">LOGO</div>
  <div class="abs account"><span>User Login</span><span>Sign Up</span></div>
  <div class="abs search-label">Search</div>
  <div class="abs search-field"></div>
  <div class="abs search-go">GO</div>

  <nav class="nav">
    <a class="is-active" style="left:38px;width:88px">HOME</a>
    <a style="left:194px;width:88px">GALLERY</a>
    <a style="left:349px;width:98px">QUESTIONS</a>
    <a style="left:503px;width:90px">ORDER</a>
    <a style="left:659px;width:128px">SHOPPINGCART</a>
  </nav>

  <div class="abs video" role="img" aria-label="Installation video player"></div>
  <svg class="abs" style="left:296px;top:373px" width="40" height="40" viewBox="0 0 40 40" aria-hidden="true">
    <circle cx="20" cy="20" r="18" fill="#4a4a4a" stroke="#c8c8c8" stroke-width="3"/>
    <path d="M15 11 L29 20 L15 29 Z" fill="#e8e8e8"/>
  </svg>

  <p class="abs intro" style="top:254px">The website is currently under construction. It will be online soon.Thank you for your patien ce while we build our website The website is currently under construction. It will be online soon.Thank you for your patien ce while we build our website..</p>
  <p class="abs intro" style="top:405px">The website is currently under construction. It will be online soon.Thank you for your patien ce while we build our website The website is currently under construction. It will be online soon.Thank you for your patien ce while we build our website..</p>

  <section class="abs card" style="left:38px;width:268px">
    <div class="card-photo" role="img" aria-label="Granite kitchen countertop with wooden cabinets" style="left:19px;width:215px;background:linear-gradient(160deg,#8a4a2a,#b98a5c 55%,#cdb08a)"></div>
    <div class="card-button" style="left:22px;width:217px">QUESTIONS
      <svg width="22" height="18" viewBox="0 0 22 18"><path d="M2 2l7 7-7 7M11 2l7 7-7 7" fill="none" stroke="#333" stroke-width="3"/></svg></div>
  </section>
  <section class="abs card" style="left:325px;width:256px">
    <div class="card-photo" role="img" aria-label="Close-up of a polished granite countertop edge" style="left:18px;width:204px;background:linear-gradient(150deg,#5a4a30,#2d2a22 55%,#b37a4a)"></div>
    <div class="card-button" style="left:16px;width:222px;font-size:18px">COLOR SELECTION
      <svg width="22" height="18" viewBox="0 0 22 18"><path d="M2 2l7 7-7 7M11 2l7 7-7 7" fill="none" stroke="#333" stroke-width="3"/></svg></div>
  </section>
  <section class="abs card" style="left:600px;width:250px">
    <div class="card-photo" role="img" aria-label="Granite counter with stainless steel sink" style="left:32px;width:189px;background:linear-gradient(170deg,#b88a55,#a68a6a 50%,#7a5230)"></div>
    <div class="card-button" style="left:20px;width:218px">GET A QUOTE
      <svg width="22" height="18" viewBox="0 0 22 18"><path d="M2 2l7 7-7 7M11 2l7 7-7 7" fill="none" stroke="#333" stroke-width="3"/></svg></div>
  </section>

  <p class="abs about">The website is currently under construction. It will be online soon.Thank you for your patience while we build our website The website is currently under construction. It will be online soon.Thank you for your patience while we build our website..<br>The website is currently under construction. It will be online soon.Thank you for your patience while we build our website The website is currently under construction. It will be online soon.Thank you for your patience while we build our website..</p>

  <footer>
    <div class="abs footer"></div>
    <ul class="abs footer-links" style="left:97px;width:160px;top:988px">
      <li>HOME</li><li>GALLERY</li><li>QUESTIONS</li><li>ORDER</li><li>SHOPPINGCART</li>
    </ul>
    <ul class="abs footer-links" style="left:334px;width:200px;top:984px">
      <li>RETURN POLICY</li><li>SHIPPING POLICY</li><li>TERMS OF USE</li><li>PRIVACY</li><li>CUSTOMER SERVICE</li>
    </ul>
    <div class="abs logo logo--footer">LOGO</div>
    <div class="abs copyright">Copyright © 2011. All Rights Reserved. <span>Privacy Policy</span></div>
  </footer>
</body>
</html>
```